Online medical reviews website needs banner advert!

We need banner advert templates for our website, www.wardplume.com. These should meet the technical requirements of our partner (uploaded).

Our groundbreaking website allows doctors in training to rate and review their training.

The adverts should use the same modern design language and colour scheme as our website. They should use the text 'Help a junior doctor make a big decision - rate your training!'.

Vector assets should be supplied, allowing us to use alternative text in future.
Updates

Industry/Entity Type

Healthcare

Font styles to use
Other font styles liked:
• Karla

Colors
3277b5
0555a3
ffffff

Requirements
Must have
• Similar design to our website. Should be elegant & modern. Must allow future text to be easily inserted.
Should not have
• Unrelated design.

```html
<!DOCTYPE html>
<html lang="en">
<head>
<meta charset="utf-8">
<title>Ward Plume banner</title>
<link href="https://fonts.googleapis.com/css2?family=Karla:wght@400;700&display=swap" rel="stylesheet">
<style>
  :root {
    --brand-blue: #3277b5;
    --brand-blue-dark: #0555a3;
    --white: #ffffff;
    --sky-top: #9fb2c4;
    --sky-mid: #c9d3da;
    --hill-green: #7a7a4c;
    --hill-dark: #4f5a3a;
  }
  html, body {
    margin: 0;
    padding: 0;
    width: 1200px;
    height: 148px;
    overflow: hidden;
    background: var(--white);
  }
  .banner {
    position: relative;
    width: 1200px;
    height: 148px;
    overflow: hidden;
    font-family: "Karla", Arial, sans-serif;
  }
  .banner__scene {
    position: absolute;
    inset: 0;
    background:
      linear-gradient(180deg, rgba(0,0,0,0) 55%, rgba(40,45,25,0.25) 100%),
      linear-gradient(180deg, var(--sky-top) 0%, var(--sky-mid) 38%, #a9a78a 55%, var(--hill-green) 75%, var(--hill-dark) 100%);
  }
  .banner__content {
    position: absolute;
    inset: 0;
    display: flex;
    flex-direction: column;
    align-items: center;
  }
  .banner__headline {
    margin: 12px 0 0;
    color: var(--white);
    font-weight: 700;
    font-size: 36px;
    line-height: 1;
    letter-spacing: 0.2px;
    text-shadow: 0 1px 3px rgba(0,0,0,0.25);
  }
  .banner__cta {
    margin-top: 17px;
    width: 338px;
    height: 36px;
    display: flex;
    align-items: center;
    justify-content: center;
    background: var(--brand-blue);
    border: 1px solid var(--brand-blue-dark);
    color: var(--white);
    font-weight: 700;
    font-size: 20px;
    text-decoration: none;
    box-sizing: border-box;
  }
  .banner__url {
    margin-top: 12px;
    color: var(--white);
    font-size: 17px;
    letter-spacing: 0.3px;
  }
</style>
</head>
<body>
  <div class="banner">
    <div class="banner__scene" role="img" aria-label="Photograph of green rolling hills under a pale cloudy sky"></div>
    <div class="banner__content">
      <h1 class="banner__headline">Help a junior doctor make a big decision …</h1>
      <a class="banner__cta" href="#">Rate &amp; review your training!</a>
      <div class="banner__url">http://www.wardplume.com/</div>
    </div>
  </div>
</body>
</html>
```